Harbor Lanterns Book Cover Design featuring a Phoenix and Flames

Please design the front cover of a book called Harbor Lanterns
By YOU!
Quiet Orchard Series
Book dimensions: 2150 x 1400mm
I am really open to design styles. I would like it to be powerful with a Phoenix and fire or even a woman's form. I may have gold leaf embossed on the cover if gold is used on the wings.
I have uploaded the logo should you wish to add this. Let me know if you have any questions.
Black as a colour is great too.
- Phoenix

```html
<!DOCTYPE html>
<html lang="en">
<head>
<meta charset="utf-8">
<title>Harbor Lanterns — Book Cover</title>
<link rel="stylesheet" href="https://fonts.googleapis.com/css2?family=Cinzel:wght@400;600;700&display=swap">
<style>
  :root {
    --ink-dark: #1f0d06;
    --ember-brown: #2e1409;
    --flame-deep: #b8410f;
    --flame-orange: #ee6e1e;
    --flame-amber: #f8a23a;
    --flame-gold: #ffd867;
    --flame-white: #fff3c4;
    --series-red: #e4502c;
    --title-ivory: #f3e8dc;
    --title-shade: #a89281;
  }
  * { margin: 0; padding: 0; box-sizing: border-box; }
  html, body {
    width: 900px;
    height: 1200px;
    overflow: hidden;
    background: var(--ink-dark);
  }
  .book-cover {
    position: relative;
    width: 900px;
    height: 1200px;
    overflow: hidden;
    font-family: "Cinzel", "Trajan Pro", serif;
  }

  /* Artwork area: phoenix and flames */
  .cover-art {
    position: absolute;
    inset: 0;
    overflow: hidden;
    background:
      radial-gradient(ellipse 70% 60% at 75% 45%, #3b1a0b 0%, var(--ember-brown) 60%, var(--ink-dark) 100%);
  }
  .cover-art__wing {
    position: absolute;
    left: -140px;
    top: -60px;
    width: 900px;
    height: 560px;
    transform: rotate(22deg);
    background:
      radial-gradient(ellipse 48% 42% at 62% 55%, var(--flame-white) 0%, var(--flame-gold) 14%, var(--flame-amber) 32%, var(--flame-orange) 50%, var(--flame-deep) 66%, transparent 74%);
    filter: blur(4px);
    opacity: 0.95;
  }
  .cover-art__wing-tip {
    position: absolute;
    left: -80px;
    top: 40px;
    width: 520px;
    height: 260px;
    transform: rotate(8deg);
    background:
      radial-gradient(ellipse 50% 45% at 50% 50%, var(--flame-amber) 0%, var(--flame-orange) 40%, rgba(184, 65, 15, 0.7) 65%, transparent 75%);
    filter: blur(6px);
  }
  .cover-art__body {
    position: absolute;
    left: 600px;
    top: 300px;
    width: 230px;
    height: 560px;
    transform: rotate(14deg);
    background:
      radial-gradient(ellipse 46% 48% at 50% 40%, var(--flame-white) 0%, var(--flame-gold) 25%, var(--flame-amber) 48%, var(--flame-orange) 62%, transparent 72%);
    filter: blur(5px);
  }
  .cover-art__flames {
    position: absolute;
    left: 0;
    right: 0;
    bottom: 0;
    height: 470px;
    background:
      radial-gradient(ellipse 30% 55% at 85% 95%, var(--flame-gold) 0%, var(--flame-amber) 30%, transparent 70%),
      radial-gradient(ellipse 35% 50% at 30% 100%, var(--flame-amber) 0%, var(--flame-orange) 35%, transparent 75%),
      linear-gradient(0deg, var(--flame-orange) 0%, #d2521a 25%, rgba(170, 55, 15, 0.75) 55%, rgba(90, 30, 10, 0.3) 80%, transparent 100%);
  }
  .cover-art__title-shadow {
    position: absolute;
    left: 80px;
    top: 780px;
    width: 740px;
    height: 280px;
    background: radial-gradient(ellipse 50% 50% at 50% 50%, rgba(30, 10, 4, 0.55), transparent 75%);
  }

  /* Series name */
  .series-mark {
    position: absolute;
    top: 566px;
    left: 0;
    width: 100%;
    display: flex;
    flex-direction: column;
    align-items: center;
    gap: 22px;
  }
  .series-mark__dot {
    width: 86px;
    height: 86px;
    border-radius: 50%;
    background: var(--series-red);
  }
  .series-mark__name {
    color: var(--series-red);
    font-weight: 600;
    font-size: 36px;
    letter-spacing: 2px;
    line-height: 1;
  }

  /* Title */
  .book-title {
    position: absolute;
    top: 772px;
    left: 0;
    width: 100%;
    text-align: center;
    color: var(--title-ivory);
    font-weight: 700;
    line-height: 0.92;
    text-shadow:
      0 2px 0 var(--title-shade),
      0 5px 12px rgba(0, 0, 0, 0.8);
  }
  .book-title__line { display: block; }
  .book-title__line--first { font-size: 142px; }
  .book-title__line--second { font-size: 122px; }

  .author-name {
    position: absolute;
    top: 1122px;
    left: 0;
    width: 100%;
    text-align: center;
    color: var(--title-ivory);
    font-weight: 600;
    font-size: 38px;
    letter-spacing: 1px;
    text-shadow: 0 2px 6px rgba(0, 0, 0, 0.75);
  }
</style>
</head>
<body>
  <main class="book-cover">
    <div class="cover-art" role="img" aria-label="Fiery phoenix with wide flaming wings sweeping across the top, its glowing body rising on the right above a bed of roaring flames on a dark ember background">
      <div class="cover-art__wing-tip" aria-hidden="true"></div>
      <div class="cover-art__wing" aria-hidden="true"></div>
      <div class="cover-art__body" aria-hidden="true"></div>
      <div class="cover-art__flames" aria-hidden="true"></div>
      <div class="cover-art__title-shadow" aria-hidden="true"></div>
    </div>

    <div class="series-mark">
      <span class="series-mark__dot"></span>
      <span class="series-mark__name">QUIET ORCHARD SERIES</span>
    </div>

    <h1 class="book-title">
      <span class="book-title__line book-title__line--first">HARBOR</span>
      <span class="book-title__line book-title__line--second">LANTERNS</span>
    </h1>

    <p class="author-name">Author Name</p>
  </main>
</body>
</html>
```